B2B Service Company - Word Template

We need a word template to be used as business proposals for prospective clients. Please visit our web site: www.quendapro.com.do and our Instagram Quendard for content / design ideas and to understand our branding and messaging . The color scheme must consistent with our logo, website and possibly our Instagram.

Just to be extra clear we expect the deliverable to be an actual working Microsoft word template document, with configured headers, theme, style, etc.

Target Market(s)

B2B Profesional companies

Requirements
Must have
• The color scheme must consistent with our logo, website and possibly our Instagram.

Different section headers, cover page with profesional design, back page, index section,

```html
<!DOCTYPE html>
<html lang="es">
<head>
<meta charset="utf-8">
<title>Quendapro – Plantilla de propuesta</title>
<link href="https://fonts.googleapis.com/css2?family=Rubik:wght@400;500;600;700&family=Roboto:wght@400;500;700&display=swap" rel="stylesheet">
<style>
:root{
  --navy:#1d2b6b;
  --teal:#45c1cd;
  --teal-soft:#c9f6fa;
  --ink:#222;
  --grey:#5e5e5e;
  --grey-light:#f1f1f1;
  --rule:#cfcfcf;
  --body:#666;
}
*{box-sizing:border-box;margin:0;padding:0}
html,body{width:1138px;height:1200px;overflow:hidden;background:#000}
body{position:relative;font-family:Roboto,sans-serif;color:var(--ink)}
.page{position:absolute;width:268px;height:381px;background:#fff;overflow:hidden}
.abs{position:absolute}
.num{position:absolute;left:0;top:8px;width:18px;height:13px;background:var(--teal);color:#fff;font:600 7px Rubik,sans-serif;display:flex;align-items:center;justify-content:center}
.ttl{position:absolute;left:22px;top:10px;color:var(--teal);font:500 7.5px Rubik,sans-serif}
.hrule{position:absolute;left:0;right:8px;top:21px;height:1px;background:var(--rule)}
.brand{position:absolute;right:8px;top:6px;text-align:right}
.brand b{display:block;font:700 8px Rubik,sans-serif;letter-spacing:.4px;color:var(--ink)}
.brand i{display:block;font:400 3px Rubik,sans-serif;font-style:normal;color:var(--ink)}
.ftr{position:absolute;left:0;right:0;bottom:0;height:10px;background:#222;color:#fff;font:700 4px Roboto,sans-serif;display:flex;justify-content:space-between;align-items:center;padding:0 5px}
.tiny{font-size:3.6px;line-height:1.45;color:var(--body)}
.teal{color:var(--teal)}
.lorem{font-size:3.8px;line-height:1.5;color:var(--body)}
.ph{position:absolute}
.toc li{list-style:none;position:absolute;left:70px;right:14px;font-size:5.2px;color:#444;display:flex;justify-content:space-between}
.toc-watermark{position:absolute;left:-92px;top:160px;width:260px;transform:rotate(-90deg);font:700 28px Rubik,sans-serif;color:#ececec;white-space:nowrap}
.sum-tbl{position:absolute;left:10px;width:246px;top:47px;border-collapse:collapse;font-size:3.8px}
.sum-tbl th{background:#9a9a9a;color:#fff;text-align:left;font-weight:700;width:44px;padding:1.6px 3px;border-bottom:1px solid #fff}
.sum-tbl td{padding:1.6px 3px;border-bottom:1px solid #eee;color:#555}
h4.sm{font:700 4.2px Roboto,sans-serif;color:var(--ink);margin-bottom:1.5px}
ul.dot{list-style:none}
ul.dot li{position:relative;padding-left:6px;margin-bottom:1.2px}
ul.dot li:before{content:"";position:absolute;left:1px;top:1.2px;width:2.4px;height:2.4px;border-radius:50%;background:#555}
.tst{position:absolute;left:11px;width:243px;top:68px;border-collapse:collapse;font-size:3.6px}
.tst thead th{background:#666;color:#fff;text-align:left;padding:3px 5px;font-weight:500}
.tst td{vertical-align:top;padding:4px 5px;color:#666;line-height:1.5}
.tst tr:nth-child(odd) td{background:var(--grey-light)}
.cert{position:absolute;left:13px;width:242px;top:65px;border-collapse:collapse}
.cert th{background:#555;color:#fff;font:500 4.6px Roboto,sans-serif;text-align:left;padding:3px 25px}
.cert td{background:var(--grey-light);height:42px;border-bottom:1px solid #fff;vertical-align:middle;font-size:5px;color:#444;line-height:1.3}
.cert td:first-child{width:110px;padding-left:20px}
.cert td b{font:700 7px Rubik,sans-serif;letter-spacing:.3px;color:var(--ink);display:block}
.cert td i{font:400 2.6px Rubik,sans-serif;font-style:normal;color:var(--ink)}
.imrow{position:absolute;left:11px;width:240px;height:77px;display:flex}
.imrow .pic{width:113px;height:100%}
.imrow .txt{flex:1;padding:6px 5px;position:relative}
.imrow .txt h5{font:700 4.3px Roboto,sans-serif;color:var(--ink);line-height:1.3;margin-bottom:2px}
.txt.cy{background:var(--teal-soft)}
.txt.gy{background:#ececec;text-align:right}
.txt.gy p{text-align:left}
.notch-l:before{content:"";position:absolute;left:-4px;top:8px;border:4px solid transparent;border-right-color:var(--teal-soft);border-left:0}
.notch-r:after{content:"";position:absolute;right:-4px;top:8px;border:4px solid transparent;border-left-color:#ececec;border-right:0}
.photo-dark{background:linear-gradient(135deg,#3c342d,#1f1c1a 60%,#4a443e)}
</style>
</head>
<body>

<section class="page" style="left:7px;top:8px">
  <div class="ph" role="img" aria-label="Fotografía de escritorio de oficina con documentos y portátil en tono azul" style="left:0;top:0;width:268px;height:230px;background:linear-gradient(160deg,#2a3a80,#1c2a66 55%,#172257)"></div>
  <div class="abs" style="right:22px;top:124px;text-align:right;font:700 9.6px/1.42 Rubik,sans-serif;color:#fff">
    HACEMOS EL TRABAJO, PARA QUE<br>TE <span class="teal">PUEDAS ENFOCAR EN LO QUE</span><br><span class="teal">REALMENTE</span> ES IMPORTANTE<br>– TU NEGOCIO.
  </div>
  <div class="abs" style="right:22px;top:264px;font:500 7.2px Rubik,sans-serif;text-align:right">PERSENTATOR NAME</div>
  <div class="abs teal" style="right:22px;top:275px;font:500 8.5px Rubik,sans-serif">XXX</div>
  <div class="abs" style="right:22px;top:318px;text-align:left">
    <div style="font:700 17px Rubik,sans-serif;letter-spacing:.8px">QUENDAPRO</div>
    <div style="font:400 6.4px Rubik,sans-serif;margin-top:-1px">soluciones para tu empresa</div>
  </div>
</section>

<section class="page toc" style="left:291px;top:8px">
  <div class="num">01</div><div class="ttl">Table of Contents</div><div class="hrule"></div>
  <div class="brand"><b>QUENDAPRO</b><i>soluciones para tu empresa</i></div>
  <div class="toc-watermark">Table of Contents</div>
  <ul>
    <li style="top:50px"><span>1&nbsp;&nbsp;&nbsp;Executive Summary</span><span>001</span></li>
    <li style="top:68px"><span>2&nbsp;&nbsp;&nbsp;XCV Scope of Work</span><span>001</span></li>
    <li style="top:87px"><span>3&nbsp;&nbsp;&nbsp;Pricing Sheets</span><span>003</span></li>
    <li style="top:106px"><span>4&nbsp;&nbsp;&nbsp;XDE QA/QC Overview</span><span>004</span></li>
    <li style="top:124px"><span>5&nbsp;&nbsp;&nbsp;Clarifications</span><span>005</span></li>
    <li style="top:143px"><span>6&nbsp;&nbsp;&nbsp;Exceptions</span><span>006</span></li>
    <li style="top:161px"><span>7&nbsp;&nbsp;&nbsp;Team Organizational Chart</span><span>006</span></li>
    <li style="top:180px"><span>8&nbsp;&nbsp;&nbsp;Resumes</span><span>006</span></li>
    <li style="top:199px"><span>9&nbsp;&nbsp;&nbsp;Certifications</span><span>007</span></li>
    <li style="top:217px"><span>10&nbsp;&nbsp;Project Plan and Schedule</span><span>008</span></li>
    <li style="top:236px"><span>11&nbsp;&nbsp;Past Project Experience</span><span>008</span></li>
    <li style="top:254px"><span>12&nbsp;&nbsp;NCE Reference Documents</span><span>008</span></li>
    <li style="top:268px"><span>&nbsp;&nbsp;&nbsp;&nbsp;&nbsp;&nbsp;&nbsp;Equipment Checklists</span><span>008</span></li>
    <li style="top:281px"><span>&nbsp;&nbsp;&nbsp;&nbsp;&nbsp;&nbsp;&nbsp;Resumes</span><span>008</span></li>
    <li style="top:299px"><span>13&nbsp;&nbsp;Mandatory Customer Documents</span><span>008</span></li>
  </ul>
  <div class="ftr"><span>Copyright text here</span><span>Page : 01</span></div>
</section>

<section class="page" style="left:571px;top:8px">
  <div class="num">01</div><div class="ttl">Table of Contents</div><div class="hrule"></div>
  <div class="brand"><b>QUENDAPRO</b><i>soluciones para tu empresa</i></div>
  <div class="abs teal" style="left:11px;top:38px;font:500 5.2px Rubik,sans-serif">PROJECT SUMMARY</div>
  <table class="sum-tbl">
    <tr><th>Title Name</th><td>Text here</td></tr>
    <tr><th>Project :</th><td>Text here</td></tr>
    <tr><th>Start Date :</th><td>October 7, 2020</td></tr>
    <tr><th>NCE Start :</th><td>Date April 15, 2021</td></tr>
    <tr><th>End Date :</th><td>December 15, 2021</td></tr>
    <tr><th>Job Description :</th><td>text here text here text here</td></tr>
  </table>
  <div class="abs tiny" style="left:9px;right:10px;top:108px;color:#444">
    <h4 class="sm">BACKGROUND/OVERVIEW</h4>
    <p>The purpose of this project is to add a temporary line terminal between the Coastline Power Co. and Elm Street Substations.</p>
    <p style="margin-top:4px">The project consists of a new 69 KV line terminal including one (1) 69 KV SF6 Gas Circuit Breaker, three (3) CVTs, three (3) surge arrestors, and two (2) gang operated disconnect switches. The new line terminal will tap into the existing #1-69 KV Bus which has two (2) existing 69 KV SF6 Gas Circuit Breakers and a 40 MVA 69-12KV Power Transformer. The bus, transformer, and breaker failure schemes for the existing equipment will be modified to include additional of CB-R.</p>
    <h4 class="sm" style="margin-top:5px">PROJECT OBJECTIVES</h4>
    <p style="color:#222;font-weight:700">✓ New Equipment in Substation</p>
    <ul class="dot" style="margin-left:4px">
      <li>Verify all newly installed equipment is safe to energize by completing all recommended electrical apparatus testing as outlined by the manufacturers, NETC, and the customer</li>
      <li>Verify all protection &amp; control schemes operate as per design.
        <ul class="dot"><li>All relay inputs and outputs will be verified through field device tests and dynamic functional testing.</li></ul></li>
      <li>Verify all SCADA signals
        <ul class="dot"><li>Verify all field equipment status points by operating equipment</li><li>Verify customer can operate all breakers and relay automation</li><li>Verify analog signals via secondary injection</li></ul></li>
      <li>Place equipment in-service
        <ul class="dot"><li>Verify primary and secondary phasing.</li><li>Take load readings after equipment is placed in-service
          <ul class="dot"><li>Verify remote terminal ends of the 69 KV lines match signals locally</li><li>Verify transformer operating and restraint current.</li><li>Verify bus differential operating current</li></ul></li></ul></li>
    </ul>
    <p style="color:#222;font-weight:700">✓ Existing Equipment in Substation</p>
    <ul class="dot" style="margin-left:8px">
      <li>Verify all cross trips and block closes between existing breakers and new breaker function properly</li>
      <li>Verify new breaker status's and CT-wiring to existing protection systems</li>
      <li>Upload new relay setting to existing protection relays</li>
    </ul>
  </div>
  <div class="ftr"><span>Copyright text here</span><span>Page : 01</span></div>
</section>

<section class="page" style="left:850px;top:8px">
  <div class="num">01</div><div class="ttl">Table of Contents</div><div class="hrule"></div>
  <div class="brand"><b>QUENDAPRO</b><i>soluciones para tu empresa</i></div>
  <div class="abs teal" style="left:11px;top:36px;font:500 4.2px Rubik,sans-serif">TABLE HEADING HERE</div>
  <div class="abs tiny" style="left:11px;right:14px;top:42px;color:#333;font-size:4px">The purpose of this project is to add a temporary line terminal between the Coastline Power Co. and Elm Street Substations.</div>
  <table class="tst">
    <thead><tr><th>Title hrere</th><th>Title hrere</th><th>QTY</th><th>Tests Included</th></tr></thead>
    <tbody>
      <tr><td>061RB RLY-311C</td><td>RLY-311C</td><td>1</td><td>1. Upload relay setting file<br>2. Test all enabled protection elements via secondary injection<br>3. Verify all relay outputs via functional checks<br>4. Verify all relay inputs via functional checks<br>5. Verify SCADA inputs/outputs<br>6. End-to-End Testing</td></tr>
      <tr><td>061RB RLY-311C</td><td>RLY-311C</td><td>1</td><td>1. Upload relay setting file<br>2. Test all enabled protection elements via secondary injection<br>3. Verify all relay outputs via functional checks<br>4. Verify all relay inputs via functional checks<br>5. Verify SCADA inputs/outputs<br>6. End-to-End Testing</td></tr>
      <tr><td>061RB RLY-311C</td><td>RLY-311C</td><td>1</td><td>1. Upload relay setting file<br>2. Test all enabled protection elements via secondary injection<br>3. Verify all relay outputs via functional checks<br>4. Verify all relay inputs via functional checks<br>5. Verify SCADA inputs/outputs<br>6. End-to-End Testing</td></tr>
      <tr><td>061RB RLY-311C</td><td>RLY-311C</td><td>1</td><td>1. Upload relay setting file<br>2. Test all enabled protection elements via secondary injection<br>3. Verify all relay outputs via functional checks<br>4. Verify all relay inputs via functional checks<br>5. Verify SCADA inputs/outputs<br>6. End-to-End Testing</td></tr>
      <tr><td>061RB RLY-311C</td><td>RLY-311C</td><td>1</td><td>1. Upload relay setting file<br>2. Test all enabled protection elements via secondary injection<br>3. Verify all relay outputs via functional checks<br>4. Verify all relay inputs via functional checks<br>5. Verify SCADA inputs/outputs<br>6. End-to-End Testing</td></tr>
    </tbody>
  </table>
  <div class="ftr"><span>Copyright text here</span><span>Page : 01</span></div>
</section>

<section class="page" style="left:7px;top:405px">
  <div class="num">01</div><div class="ttl">Table of Contents</div><div class="hrule"></div>
  <div class="brand"><b>QUENDAPRO</b><i>soluciones para tu empresa</i></div>
  <div class="abs" style="left:15px;top:41px;width:246px;height:160px;border:1px solid #e2e2e2"></div>
  <div class="abs" style="left:17px;top:43px;width:242px;height:15px;background:var(--teal);color:#fff;font:500 5.4px Rubik,sans-serif;padding:4px 6px">Project Title hrere</div>
  <div class="abs" style="left:25px;top:58px;border:3px solid transparent;border-top-color:var(--teal)"></div>
  <div class="abs tiny" style="left:23px;right:14px;top:70px">
    <p style="font:500 5.6px Rubik,sans-serif;color:#222;margin-bottom:3px"><span class="teal">✓</span> Project Title hrere</p>
    <div style="margin-left:8px">
      <h4 class="sm">✓ CB-R</h4><ul class="dot"><li>Insulation Power Factor, Time/Travel Analysis, Contact Resistance, SF6 Gas Fill and Analysis, Current Transformer (Polarity, Saturation, Turns Ratio, Winding Resistance, Insulation Resistance)</li></ul>
      <h4 class="sm">✓ CVTs</h4><ul class="dot"><li>Insulation Power Factor, Turns Ratio, Insulation Resistance</li></ul>
      <h4 class="sm">✓ Surge Arrestors</h4><ul class="dot"><li>Insulation Power Factor, Insulation Resistance</li></ul>
      <h4 class="sm">✓ CB-R</h4><ul class="dot"><li>Insulation Power Factor, Time/Travel Analysis, Contact Resistance, SF6 Gas Fill and Analysis, Current Transformer (Polarity, Saturation, Turns Ratio, Winding Resistance, Insulation Resistance)</li></ul>
      <h4 class="sm">✓ CVTs</h4><ul class="dot"><li>Insulation Power Factor, Turns Ratio, Insulation Resistance</li></ul>
      <h4 class="sm">✓ Surge Arrestors</h4><ul class="dot"><li>Insulation Power Factor, Insulation Resistance</li></ul>
    </div>
  </div>
  <div class="ftr"><span>Copyrigh text here</span><span>Page : 01</span></div>
</section>

<section class="page" style="left:291px;top:405px">
  <div class="num">01</div><div class="ttl">Table of Contents</div><div class="hrule"></div>
  <div class="brand"><b>QUENDAPRO</b><i>soluciones para tu empresa</i></div>
  <div class="abs" style="left:10px;top:35px;font:500 6px Rubik,sans-serif">Testing Table Outline</div>
  <div class="abs" style="left:8px;top:47px;width:250px;height:19px;background:var(--teal);color:#fff;font:500 6.4px Rubik,sans-serif;padding:5px 7px">Table Data Here</div>
  <div class="abs" style="left:8px;top:66px;width:250px;height:268px;border:1px solid #e8e8e8"></div>
  <div class="abs" style="left:9px;top:67px;width:248px;height:60px;background:var(--grey-light)"></div>
  <div class="abs" style="left:9px;top:196px;width:248px;height:70px;background:var(--grey-light)"></div>
  <div class="abs lorem" style="left:14px;right:16px;top:75px">
    <p class="teal" style="font:500 6px Rubik,sans-serif">Paragraph titl ehrer</p>
    <p>Lorem dolor sit ipsum Lorem dolor sit ipsum Lorem dolor sit ipsum Lorem dolor sit ipsum Lorem dolor sit ipsum Lorem dolor sit ipsum Lorem dolor sit ipsum Lorem dolor sit ipsum Lorem dolor sit ipsum Lorem dolor sit ipsum Lorem dolor sit ipsum Lorem dolor sit ipsum Lorem dolor sit ipsum Lorem dolor sit ipsum Lorem dolor sit ipsum Lorem dolor sit ipsum Lorem dolor sit ipsum Lorem dolor sit ipsum</p>
  </div>
  <div class="abs lorem" style="left:14px;right:16px;top:138px">
    <p class="teal" style="font:500 6px Rubik,sans-serif">Paragraph titl ehrer</p>
    <p>Lorem dolor sit ipsum Lorem dolor sit ipsum Lorem dolor sit ipsum Lorem dolor sit ipsum Lorem dolor sit ipsum Lorem dolor sit ipsum Lorem dolor sit ipsum Lorem dolor sit ipsum Lorem dolor sit ipsum Lorem dolor sit ipsum Lorem dolor sit ipsum Lorem dolor sit ipsum Lorem dolor sit ipsum Lorem dolor sit ipsum Lorem dolor sit ipsum Lorem dolor sit ipsum Lorem dolor sit ipsum</p>
  </div>
  <div class="abs lorem" style="left:14px;right:16px;top:209px">
    <p class="teal" style="font:500 6px Rubik,sans-serif">Paragraph titl ehrer</p>
    <p>Lorem dolor sit ipsum Lorem dolor sit ipsum Lorem dolor sit ipsum Lorem dolor sit ipsum Lorem dolor sit ipsum Lorem dolor sit ipsum Lorem dolor sit ipsum Lorem dolor sit ipsum Lorem dolor sit ipsum Lorem dolor sit ipsum Lorem dolor sit ipsum Lorem dolor sit ipsum Lorem dolor sit ipsum Lorem dolor sit ipsum Lorem dolor sit ipsum Lorem dolor sit ipsum Lorem dolor sit ipsum</p>
  </div>
  <div class="abs lorem" style="left:14px;right:16px;top:278px">
    <p class="teal" style="font:500 6px Rubik,sans-serif">Paragraph titl ehrer</p>
    <p>Lorem dolor sit ipsum Lorem dolor sit ipsum Lorem dolor sit ipsum Lorem dolor sit ipsum Lorem dolor sit ipsum Lorem dolor sit ipsum Lorem dolor sit ipsum Lorem dolor sit ipsum Lorem dolor sit ipsum Lorem dolor sit ipsum Lorem dolor sit ipsum Lorem dolor sit ipsum Lorem dolor sit ipsum Lorem dolor sit ipsum Lorem dolor sit ipsum Lorem dolor sit ipsum Lorem dolor sit ipsum</p>
  </div>
  <div class="ftr"><span>Copyrig htext here</span><span>Page : 01</span></div>
</section>

<section class="page" style="left:571px;top:405px">
  <div class="num">01</div><div class="ttl">Table of Contents</div><div class="hrule"></div>
  <div class="brand"><b>QUENDAPRO</b><i>soluciones para tu empresa</i></div>
  <div class="abs lorem" style="left:10px;right:12px;top:37px">
    <p class="teal" style="font:500 6px Rubik,sans-serif">Paragraph titl ehrer</p>
    <p>Lorem dolor sit ipsum Lorem dolor sit ipsum Lorem dolor sit ipsum Lorem dolor sit ipsum Lorem dolor sit ipsum Lorem dolor sit ipsum Lorem dolor sit ipsum Lorem dolor sit ipsum Lorem dolor sit ipsum Lorem dolor sit ipsum Lorem dolor sit ipsum Lorem dolor sit ipsum Lorem dolor sit ipsum Lorem dolor sit ipsum Lorem dolor sit ipsum Lorem dolor sit ipsum Lorem dolor sit ipsum Lorem dolor sit ipsum Lorem dolor sit ipsum Lorem dolor sit ipsum</p>
    <p style="margin-top:5px">Lorem dolor sit ipsum Lorem dolor sit ipsum Lorem dolor sit ipsum Lorem dolor sit ipsum Lorem dolor sit ipsum Lorem dolor sit ipsum Lorem dolor sit ipsum Lorem dolor sit ipsum Lorem dolor sit ipsum Lorem dolor sit ipsum Lorem dolor sit ipsum Lorem dolor sit ipsum Lorem dolor sit ipsum Lorem dolor sit ipsum Lorem dolor sit ipsum Lorem dolor sit ipsum Lorem dolor sit ipsum Lorem dolor sit ipsum</p>
    <p style="margin-top:5px">Lorem dolor sit ipsum Lorem dolor sit ipsum Lorem dolor sit ipsum Lorem dolor sit ipsum Lorem dolor sit ipsum Lorem dolor sit ipsum Lorem dolor sit ipsum Lorem dolor sit ipsum Lorem dolor sit ipsum Lorem dolor sit ipsum Lorem dolor sit ipsum Lorem dolor sit ipsum Lorem dolor sit ipsum Lorem dolor sit ipsum Lorem dolor sit ipsum Lorem dolor sit ipsum Lorem dolor sit ipsum Lorem dolor sit ipsum</p>
    <p style="margin-top:9px">Lorem dolor sit ipsum Lorem dolor sit ipsum Lorem dolor sit ipsum Lorem dolor sit ipsum Lorem dolor sit ipsum Lorem dolor sit ipsum Lorem dolor sit ipsum Lorem dolor sit ipsum Lorem dolor sit ipsum Lorem dolor sit ipsum Lorem dolor sit ipsum Lorem dolor sit ipsum Lorem dolor sit ipsum Lorem dolor sit ipsum Lorem dolor sit ipsum Lorem dolor sit ipsum Lorem dolor sit ipsum Lorem dolor sit ipsum</p>
    <p style="margin-top:5px">Lorem dolor sit ipsum Lorem dolor sit ipsum Lorem dolor sit ipsum Lorem dolor sit ipsum Lorem dolor sit ipsum Lorem dolor sit ipsum Lorem dolor sit ipsum Lorem dolor sit ipsum Lorem dolor sit ipsum Lorem dolor sit ipsum Lorem dolor sit ipsum Lorem dolor sit ipsum Lorem dolor sit ipsum Lorem dolor sit ipsum Lorem dolor sit ipsum Lorem dolor sit ipsum Lorem dolor sit ipsum Lorem dolor sit ipsum</p>
  </div>
  <div class="ftr"><span>Copyrigh text ehrer</span><span>Page : 01</span></div>
</section>

<section class="page" style="left:850px;top:405px">
  <div class="num">01</div><div class="ttl">Table of Contents</div><div class="hrule"></div>
  <div class="brand"><b>QUENDAPRO</b><i>soluciones para tu empresa</i></div>
  <div class="abs teal" style="left:0;right:0;top:44px;text-align:center;font:500 5.4px Rubik,sans-serif">TEAM ORGAZINATIONAL CHART</div>
  <div class="abs" style="left:0;right:0;top:63px;text-align:center">
    <div style="font:700 8px Rubik,sans-serif;letter-spacing:.4px">QUENDAPRO</div>
    <div style="font:400 3px Rubik,sans-serif">soluciones para tu empresa</div>
  </div>
  <svg class="abs" style="left:0;top:0" width="268" height="381" viewBox="0 0 268 381" font-family="Roboto,sans-serif">
    <defs>
      <symbol id="hx" viewBox="0 0 54 15"><polygon points="0,7.5 5,0 49,0 54,7.5 49,15 5,15"/></symbol>
    </defs>
    <g stroke="#9a9a9a" stroke-width=".5" fill="none">
      <line x1="136" y1="104" x2="136" y2="228"/>
      <path d="M128 104 Q128 112 120 112 L104 112 Q97 112 97 118"/>
      <path d="M144 104 Q144 112 152 112 L165 112 Q172 112 172 118"/>
      <path d="M97 140 Q97 148 88 148 L76 148 Q68 148 68 155"/>
      <line x1="34" y1="184" x2="239" y2="184"/>
      <line x1="34" y1="184" x2="34" y2="194"/><line x1="86" y1="184" x2="86" y2="194"/>
      <line x1="188" y1="184" x2="188" y2="194"/><line x1="239" y1="184" x2="239" y2="194"/>
    </g>
    <use href="#hx" x="109" y="88" width="54" height="16" fill="#2cc2cf"/>
    <use href="#hx" x="70" y="125" width="54" height="16" fill="#666"/>
    <use href="#hx" x="145" y="125" width="54" height="16" fill="#666"/>
    <use href="#hx" x="41" y="160" width="54" height="16" fill="#666"/>
    <g fill="#666">
      <use href="#hx" x="7" y="196" width="54" height="15"/><use href="#hx" x="59" y="196" width="54" height="15"/>
      <use href="#hx" x="110" y="196" width="54" height="15"/><use href="#hx" x="161" y="196" width="54" height="15"/>
      <use href="#hx" x="212" y="196" width="54" height="15"/>
      <use href="#hx" x="7" y="228" width="54" height="15"/><use href="#hx" x="59" y="228" width="54" height="15"/>
      <use href="#hx" x="110" y="228" width="54" height="15"/><use href="#hx" x="161" y="228" width="54" height="15"/>
      <use href="#hx" x="212" y="228" width="54" height="15"/>
    </g>
    <g fill="#fff" text-anchor="middle">
      <g font-size="3.6" font-weight="700">
        <text x="136" y="95">Main Text ehre</text><text x="97" y="132">Main Text ehre</text><text x="172" y="132">Main Text ehre</text><text x="68" y="167">Main Text ehre</text>
        <text x="34" y="203">Main Text ehre</text><text x="86" y="202">Main Text ehre</text><text x="137" y="203">Main Text ehre</text><text x="188" y="203">Main Text ehre</text><text x="239" y="203">Main Text ehre</text>
        <text x="34" y="235">Main Text ehre</text><text x="86" y="235">Main Text ehre</text><text x="137" y="235">Main Text ehre</text><text x="188" y="235">Main Text ehre</text><text x="239" y="235">Main Text ehre</text>
      </g>
      <g font-size="3.2">
        <text x="136" y="100">Chief Executive Officer</text><text x="97" y="137">Chief Executive Officer</text><text x="172" y="137">Chief Executive Officer</text><text x="68" y="172">Chief Executive Officer</text>
        <text x="34" y="208">Chief Executive Officer</text><text x="86" y="207">Chief Executive Officer</text><text x="137" y="208">Chief Executive Officer</text><text x="188" y="208">Chief Executive Officer</text><text x="239" y="208">Chief Executive Officer</text>
        <text x="34" y="240">Chief Executive Officer</text><text x="86" y="240">Chief Executive Officer</text><text x="137" y="240">Chief Executive Officer</text><text x="188" y="240">Chief Executive Officer</text><text x="239" y="240">Chief Executive Officer</text>
      </g>
    </g>
  </svg>
  <div class="ftr"><span>Copyright text here</span><span>Page : 01</span></div>
</section>

<section class="page" style="left:7px;top:797px">
  <div class="num">01</div><div class="ttl">Table of Contents</div><div class="hrule"></div>
  <div class="brand"><b>QUENDAPRO</b><i>soluciones para tu empresa</i></div>
  <div class="abs teal" style="left:15px;top:36px;font:500 4.2px Rubik,sans-serif">TABLE HEADING HERE</div>
  <div class="abs tiny" style="left:15px;right:14px;top:42px;color:#333;font-size:4px">The purpose of this project is to add a temporary line terminal between the Coastline Power Co. and Elm Street Substations.</div>
  <table class="cert">
    <thead><tr><th style="padding-left:25px">CERTIFICATION</th><th style="padding-left:12px">CERTIFYING BODY</th></tr></thead>
    <tbody>
      <tr><td><b>QUENDAPRO</b><i>soluciones para tu empresa</i></td><td style="padding-left:12px">National Electrical<br>Testing Council</td></tr>
      <tr><td><b>QUENDAPRO</b><i>soluciones para tu empresa</i></td><td style="padding-left:12px">Harlow Quality<br>Registrars</td></tr>
      <tr><td><b>QUENDAPRO</b><i>soluciones para tu empresa</i></td><td style="padding-left:12px">United Guild of<br>Electrical Workers Local Unions<br>#351, 269, 400, 456, 126, 102, 164</td></tr>
      <tr><td><b>QUENDAPRO</b><i>soluciones para tu empresa</i></td><td style="padding-left:12px">Office of<br>Veteran Services</td></tr>
    </tbody>
  </table>
  <div class="ftr"><span>Copyright text here</span><span>Page : 01</span></div>
</section>

<section class="page" style="left:289px;top:797px;width:269px">
  <div class="ph" role="img" aria-label="Fotografía de equipo de trabajo en reunión con tinte turquesa" style="left:0;top:0;width:269px;height:189px;background:linear-gradient(180deg,#7fd3db,#5bc8d3 45%,#45c1cd)"></div>
  <div class="abs" style="left:0;right:0;top:112px;text-align:center;color:#fff">
    <div style="font:700 30px Rubik,sans-serif;letter-spacing:1.5px;line-height:1">QUENDAPRO</div>
    <div style="font:400 13px Rubik,sans-serif;margin-top:2px">soluciones para tu empresa</div>
  </div>
  <div class="abs" style="left:-4px;top:270px;transform:rotate(-90deg);transform-origin:center;font:700 20px/0.95 Rubik,sans-serif;color:#ececec;white-space:nowrap;text-align:left">CONTACT<br><span style="font-size:15px">INFORMATION</span></div>
  <div class="abs" style="left:110px;top:214px;font:400 6px/1.8 Rubik,sans-serif;color:#444">
    <div class="teal" style="font:500 8px Rubik,sans-serif;margin-bottom:2px">Quendapro, SAS</div>
    Avenida Los Almendros 48,<br>Torre Marina, Piso 12,<br>República Dominicana
    <div style="margin-top:8px"><span class="teal">Tel.:</span> (809) 555-0142</div>
    <div style="margin-top:8px"><span class="teal">Email :</span> hola@quendapro.com.do</div>
  </div>
  <div class="abs teal" style="left:108px;top:345px;font:400 12px Rubik,sans-serif">www.quendapro.com.do</div>
</section>

<section class="page" style="left:569px;top:797px">
  <div class="num">01</div><div class="ttl">Our Images</div><div class="hrule"></div>
  <div class="brand"><b>QUENDAPRO</b><i>soluciones para tu empresa</i></div>
  <div class="imrow" style="top:41px">
    <div class="pic photo-dark" role="img" aria-label="Foto de manos revisando documentos sobre mesa de madera"></div>
    <div class="txt cy notch-l"><h5>Image Title hrere Image Title hrere<br>Image Title hrere</h5><p class="lorem" style="font-size:3.4px">Lorem ipsum dolor ipsum Lorem ipsum dolor ipsum Lorem ipsum dolor ipsum Lorem ipsum dolor ipsum Lorem ipsum dolor ipsum Lorem ipsum dolor ipsum Lorem ipsum dolor ipsum Lorem ipsum dolor ipsum Lorem ipsum dolor ipsum Lorem ipsum dolor ipsum Lorem ipsum dolor ipsum Lorem ipsum dolor ipsum</p></div>
  </div>
  <div class="imrow" style="top:122px">
    <div class="txt gy notch-r"><h5>Image Title hrere Image Title hrere<br>Image Title hrere</h5><p class="lorem" style="font-size:3.4px">Lorem ipsum dolor ipsum Lorem ipsum dolor ipsum Lorem ipsum dolor ipsum Lorem ipsum dolor ipsum Lorem ipsum dolor ipsum Lorem ipsum dolor ipsum Lorem ipsum dolor ipsum Lorem ipsum dolor ipsum Lorem ipsum dolor ipsum Lorem ipsum dolor ipsum</p></div>
    <div class="pic photo-dark" role="img" aria-label="Foto de escritorio con portátil, teléfono y café"></div>
  </div>
  <div class="imrow" style="top:203px">
    <div class="pic photo-dark" role="img" aria-label="Foto de reunión con gráficos impresos sobre la mesa"></div>
    <div class="txt cy notch-l"><h5>Image Title hrere Image Title hrere<br>Image Title hrere</h5><p class="lorem" style="font-size:3.4px">Lorem ipsum dolor ipsum Lorem ipsum dolor ipsum Lorem ipsum dolor ipsum Lorem ipsum dolor ipsum Lorem ipsum dolor ipsum Lorem ipsum dolor ipsum Lorem ipsum dolor ipsum Lorem ipsum dolor ipsum Lorem ipsum dolor ipsum Lorem ipsum dolor ipsum</p></div>
  </div>
  <div class="imrow" style="top:284px">
    <div class="txt gy notch-r"><h5>Image Title hrere Image Title hrere<br>Image Title hrere</h5><p class="lorem" style="font-size:3.4px">Lorem ipsum dolor ipsum Lorem ipsum dolor ipsum Lorem ipsum dolor ipsum Lorem ipsum dolor ipsum Lorem ipsum dolor ipsum Lorem ipsum dolor ipsum Lorem ipsum dolor ipsum Lorem ipsum dolor ipsum Lorem ipsum dolor ipsum Lorem ipsum dolor ipsum</p></div>
    <div class="pic photo-dark" role="img" aria-label="Foto de documentos financieros y calculadora sobre mesa"></div>
  </div>
  <div class="ftr"><span>Copyrightext here</span><span>Page : 01</span></div>
</section>

</body>
</html>
```